corvalinkto 2 page brochure

We need some design input for a corporate brochure.
PDF of the content to be designed around is as attached - and also png images used in the mockup.
This will be used for corporate marketing to senior execs in big companies - so needs to look professional and fun at the same time.
Feel free to make whatever design changes you like and we will give good feedback.
Updates
Just made this a guaranteed payment - looking forward to receiving lots of great designs!
Target Market(s)
To appeal to corporate marketing executives
Industry/Entity Type
Marketing
Look and feel
Each slider illustrates characteristics of the customer's brand and the style your logo design should communicate.

```html
<!DOCTYPE html>
<html lang="en">
<head>
<meta charset="utf-8">
<title>corvalinkto brochure</title>
<link href="https://fonts.googleapis.com/css2?family=Nunito:wght@800&family=Source+Sans+3:wght@400;600&family=Arimo&display=swap" rel="stylesheet">
<style>
:root{
  --sky-top:#34367f;
  --sky-mid:#5a5fb0;
  --sky-low:#7f88cc;
  --brand-red:#b92431;
  --white:#ffffff;
  --grey-head:#858585;
  --grey-text:#333333;
  --band-blue:#4a6cb6;
  --device:#e9ebf0;
}
*{margin:0;padding:0;box-sizing:border-box}
html,body{width:851px;height:1200px;overflow:hidden;background:#fff}
.page{position:relative;width:851px;height:1200px;overflow:hidden;
  background:linear-gradient(180deg,var(--sky-top) 0%,var(--sky-mid) 40%,var(--sky-low) 66%,#fff 78%);
  font-family:"Source Sans 3",sans-serif;color:var(--white)}
.sweep{position:absolute;left:0;top:0;width:851px;height:1200px}
.logo-mark{position:absolute;left:72px;top:70px;width:110px;height:110px;border-radius:50%;
  background:var(--white);display:flex;align-items:center;justify-content:center;
  font-family:"Nunito",sans-serif;font-weight:800;font-size:17px;color:var(--brand-red)}
.wordmark{position:absolute;left:258px;top:62px;font-family:"Nunito",sans-serif;font-weight:800;
  font-size:96px;line-height:1;color:var(--brand-red);letter-spacing:-1px}
.tagline{position:absolute;left:40px;top:226px;width:771px;text-align:center;font-size:24.5px;line-height:22px}
.section-title{position:absolute;left:82px;font-size:20.5px;font-weight:400}
.list{position:absolute;left:82px;list-style:none}
.list li::before{content:"● ";font-size:10px;vertical-align:1px}
.benefits{top:398px;font-size:12.5px;line-height:19.7px}
.benefits small,.sponsor small{font-size:10.8px}
.how{top:552px;font-family:"Arimo",sans-serif;font-size:12.5px;line-height:15.4px}
.pillar{position:absolute;top:644px;width:142px;text-align:center}
.pillar h3{font-weight:400;font-size:22px;margin-bottom:12px}
.pillar p{font-size:14px;line-height:20px;color:var(--white);text-shadow:0 1px 2px rgba(40,40,110,.45)}
.device{position:absolute;left:615px;top:333px;width:190px;height:463px;border-radius:30px;
  background:linear-gradient(160deg,#ffffff,var(--device) 60%,#c9ccd6)}
.device-screen{position:absolute;left:10px;top:76px;width:170px;height:308px;
  background:linear-gradient(180deg,#2e2e2e 0%,#3c8a2c 12%,#9aa09a 45%,#555 80%,#1e1e1e 100%)}
.platform{position:absolute;left:95px;top:814px;font-size:16px;color:var(--grey-head)}
.platform small{font-size:13px}
.sponsor-title{top:864px;color:var(--grey-head)}
.sponsor{top:911px;width:700px;color:var(--grey-text);font-size:12.5px;line-height:20px}
.band{position:absolute;left:0;top:1149px;width:851px;height:51px;background:var(--band-blue)}
.band-tab{position:absolute;left:534px;top:1102px;width:317px;height:60px;background:var(--band-blue);
  border-top-left-radius:60px 50px}
.contact{position:absolute;left:572px;top:1118px;font-size:19.5px;color:var(--white)}
</style>
</head>
<body>
<main class="page">
  <svg class="sweep" viewBox="0 0 851 1200" aria-hidden="true">
    <defs>
      <linearGradient id="sweepFill" x1="0" y1="0" x2="0" y2="1">
        <stop offset="0" stop-color="#fff" stop-opacity="0.25"/>
        <stop offset="0.12" stop-color="#fff" stop-opacity="0.9"/>
        <stop offset="0.25" stop-color="#fff"/>
      </linearGradient>
      <linearGradient id="blush" x1="0" y1="0" x2="1" y2="0">
        <stop offset="0" stop-color="#c97f9c" stop-opacity="0.45"/>
        <stop offset="1" stop-color="#c97f9c" stop-opacity="0"/>
      </linearGradient>
    </defs>
    <path d="M0 650 C250 660 500 650 851 610 L851 700 C550 750 250 770 0 790 Z" fill="url(#blush)"/>
    <path d="M0 795 C300 785 560 750 851 700 L851 1200 L0 1200 Z" fill="url(#sweepFill)"/>
  </svg>

  <div class="logo-mark">corvalinkto</div>
  <h1 class="wordmark">corvalinkto</h1>

  <p class="tagline">Corvalinkto helps organisations increase the value of their brands and media rights through inplay mobile games based on live sports events, tv talent contests and other popular events.</p>

  <h2 class="section-title" style="top:349px">Benefits of launching your own inplay mobile game</h2>
  <ul class="list benefits">
    <li>Increase engagement with your brand <small>- by associating it with popular live events</small></li>
    <li>Increase awareness of your products or servicez <small>- using in-game messaging and links</small></li>
    <li>Increase traffic to your website <small>- and increase the number of users in your database</small></li>
    <li>More effectievly target &nbsp;the right customers <small>- using rich user profile data captured by the game</small></li>
    <li>Generate additional revenue <small>- throug different game monetisation mechanisms</small></li>
  </ul>

  <h2 class="section-title" style="top:508px">Launching your own inplay mobile game - how it works</h2>
  <ul class="list how">
    <li>Our games can be easly re-skinned with your brand and launched within 2 weeks</li>
    <li>Games can be based on any live Sport Event, Reality TV Show or Political Election</li>
    <li>Launch to our existing distribution network, and leverage your own channels to market</li>
    <li>Viral game play mechanics helps the game to spread across existing social networks</li>
    <li>Prizes offered to the best performers also increases user likelihood to register and play</li>
  </ul>

  <section class="pillar" style="left:28px"><h3>Inplay</h3><p>Gameplay is driven in real-time by what happens in real-life in the events</p></section>
  <section class="pillar" style="left:166px"><h3>Social</h3><p>Integrated with Social Networks to drive social game play and viral spread</p></section>
  <section class="pillar" style="left:312px"><h3>Mobile</h3><p>Delivered through mobile companion apps (Pomphone, Droidix, Pomtab)</p></section>
  <section class="pillar" style="left:460px"><h3>Popular Events</h3><p>Games can &nbsp;currently be based on Sports, Reality TV and &nbsp;Politics</p></section>

  <div class="device" role="img" aria-label="Smartphone showing the live match prediction game screen">
    <div class="device-screen"></div>
  </div>

  <p class="platform">Multi-Tenanted Platform <small>- our platform can host multiple games - which can be launched within 2 weeks</small></p>

  <h2 class="section-title sponsor-title">Specific benefits to you - Corporate Sponsor</h2>
  <ul class="list sponsor">
    <li>Increase monetisation of your website <small>- use the game to drive traffic to your website and monetise through existing mechanisms</small></li>
    <li>Increase awareness of your registered users <small>- require players of the game to sign up &nbsp;for an acc on your website, and monotise through existing mechanisms</small></li>
    <li>Increase the value of your brand <small>- by associating it &nbsp;with a popular event with high viewer engagement</small></li>
    <li>Raise awareness of your products and services<small>- through in-game targeted messaging</small></li>
    <li>Improve the effectiveness of your direct marketing<small>- by using rich user data captured during registration and throughout gameplay</small></li>
    <li>Gain implied social endorsement of your brand<small>- due to players inviting friends through viral gameplay mechanics</small></li>
    <li>Increase awareness and positive emotion towards your brand <small>- by offering your products / services as prizes for the best players</small></li>
  </ul>

  <div class="band-tab"></div>
  <div class="band"></div>
  <p class="contact">contact@corvalinkto. com</p>
</main>
</body>
</html>
```